Roasted coffee packaging for TALL KETTLE & CO.

TALL KETTLE & CO. is a specialised coffee roasting business in Adelaide South Australia.
I am looking for eye catching packaging designs for 250g, 500g and 1kg box bottom coffee bean bags with approx. sizes as follows:
250g = Height: 240mm, Width: 100mm, Gusset/side: 65mm
500g = Height: 290mm, Width: 110mm, Gusset/side: 80mm
1kg = Height: 345mm, Width: 145mm, Gusset/side: 90mm
I had thought to use the coffee bean in the attached logo as a continuous print on the gusset/side of the bags.
Obviously the logo featured on the front of the bags, as well as a space for some information including the text: 100% Arabica.
FRESHLY ROASTED COFFEE
The attached whole bean graphic.
The light roast to dark roast indicator graphic.
The packaging weight.
On the back of the bag include space for information such as the text: "roasted on", including a box to hand write the date or stick on a label in this section.
A grind size usage guide eg. course grind for drip coffee, fine grind for espresso coffee etc. with small icons scaled from course to fine, like the attached graphics.
TIPS:
Grind - the beans immediately before brewing, this will maximise the flavour.
Extract - your coffee shot in 25 - 30 seconds aiming for 25 - 30ml of extraction.
Store - the beans in this bag, the airlock seal and valve are designed to keep your freshly roasted coffee beans at optimum quality.
Include web address: www.tallkettleandco.com.au, and manufactures address: 47 Wattle Crescent, Salisbury, SA 5108
Add the facebook symbol then the text: TALL KETTLE & CO.
Add the Instagram symbol then the text: @tall.kettle.and.co
Any other thoughts and ideas would be appreciated, looking for creative eye catching designs.
Target Market(s)
Cafes, coffee drinkers, restaurants, home coffee enthusiasts, export, retail sales, supermarkets etc.
Colors
Designer to choose colors to be used in the design.
Look and feel

```html
<!DOCTYPE html>
<html lang="en">
<head>
<meta charset="utf-8">
<title>TALL KETTLE &amp; CO. — 250g Coffee Bag Front</title>
<link rel="stylesheet" href="https://fonts.googleapis.com/css2?family=Montserrat:wght@500;600;700&display=swap">
<style>
  :root {
    --backdrop: #e9e4df;
    --bag-black: #121112;
    --bag-black-soft: #1c1b1c;
    --copper: #c9a184;
    --copper-deep: #a97f62;
    --copper-light: #dcbba3;
    --band-ink: #1a1311;
    --zip-line: #2a292a;
  }
  * { margin: 0; padding: 0; box-sizing: border-box; }
  html, body { width: 1096px; height: 1200px; overflow: hidden; }
  body {
    background: var(--backdrop);
    font-family: "Montserrat", sans-serif;
    position: relative;
  }
  .bag {
    position: absolute;
    left: 223px;
    top: 80px;
    width: 650px;
    height: 1040px;
    display: flex;
  }
  .bag-front {
    position: relative;
    width: 420px;
    height: 100%;
    background: linear-gradient(180deg, var(--bag-black-soft) 0%, var(--bag-black) 40%, var(--bag-black) 100%);
    color: var(--copper);
  }
  .bag-gusset {
    width: 230px;
    height: 100%;
    background: linear-gradient(90deg, #0c0b0c 0%, #3a2b22 35%, #6e4f3c 60%, #2a1f19 100%);
  }
  .zip-seal {
    position: absolute;
    left: 0; right: 0;
    top: 100px;
    height: 70px;
  }
  .zip-seal span {
    display: block;
    height: 2px;
    margin-bottom: 10px;
    background: var(--zip-line);
  }
  .brand-mark {
    position: absolute;
    left: 50%;
    top: 360px;
    width: 270px;
    height: 270px;
    transform: translateX(-50%);
    border: 3px solid var(--copper);
    border-radius: 50%;
    display: flex;
    align-items: center;
    justify-content: center;
    text-align: center;
  }
  .brand-name {
    font-weight: 700;
    font-size: 27px;
    line-height: 1.2;
    letter-spacing: 1px;
    color: var(--copper);
  }
  .brand-tagline {
    position: absolute;
    left: 0; right: 0;
    top: 645px;
    text-align: center;
    font-size: 11px;
    font-weight: 600;
    letter-spacing: 1.5px;
  }
  .variety-band {
    position: absolute;
    left: 0; right: 0;
    top: 700px;
    height: 44px;
    background: linear-gradient(90deg, var(--copper-deep), var(--copper) 40%, var(--copper-light) 100%);
    display: flex;
    align-items: center;
    padding-left: 110px;
    font-weight: 700;
    font-size: 18px;
    color: var(--band-ink);
  }
  .whole-bean-badge {
    position: absolute;
    left: 38px;
    top: 690px;
    width: 62px;
    height: 62px;
    border-radius: 50%;
    background: var(--bag-black);
    border: 3px solid var(--copper);
  }
  .roast-scale {
    position: absolute;
    left: 0; right: 0;
    top: 772px;
    display: flex;
    justify-content: center;
    align-items: center;
    gap: 14px;
    font-size: 11px;
    font-weight: 700;
    line-height: 1.1;
  }
  .roast-scale .scale-label--dark { text-align: right; padding-top: 14px; }
  .roast-scale .scale-label--light { padding-bottom: 14px; }
  .roast-dots { display: flex; gap: 8px; }
  .roast-dot {
    width: 12px; height: 12px;
    border: 1.5px solid var(--copper);
    border-radius: 50%;
  }
  .roast-dot--selected { background: var(--copper); }
  .tagline {
    position: absolute;
    left: 0; right: 0;
    top: 842px;
    text-align: center;
    font-weight: 700;
    font-size: 17px;
  }
  .net-weight {
    position: absolute;
    left: 0; right: 0;
    top: 950px;
    text-align: center;
    font-weight: 700;
    font-size: 17px;
    color: #e6d6c9;
  }
</style>
</head>
<body>
  <div class="bag">
    <section class="bag-front">
      <div class="zip-seal"><span></span><span></span><span></span><span></span><span></span></div>

      <div class="brand-mark">
        <p class="brand-name">TALL KETTLE<br>&amp; CO.</p>
      </div>
      <p class="brand-tagline">COFFEE ROASTERS</p>

      <div class="variety-band">100% ARABICA</div>
      <div class="whole-bean-badge"></div>

      <div class="roast-scale">
        <span class="scale-label--light">LIGHT<br>ROAST</span>
        <div class="roast-dots">
          <span class="roast-dot"></span>
          <span class="roast-dot"></span>
          <span class="roast-dot"></span>
          <span class="roast-dot roast-dot--selected"></span>
          <span class="roast-dot"></span>
          <span class="roast-dot"></span>
        </div>
        <span class="scale-label--dark">DARK<br>ROAST</span>
      </div>

      <p class="tagline">FRESHLY ROASTED COFFEE</p>
      <p class="net-weight">NET WEIGHT 250g</p>
    </section>

    <div class="bag-gusset" role="img" aria-label="Side gusset with a repeating copper coffee bean pattern on black"></div>
  </div>
</body>
</html>
```